customer services company for the travel industry needs a flyer designed

we need a flyer for our London based company. We are an outsource service to the travel industry so our client companies receive a complaint from their customer about their holiday or travel arrangements and they pass it to us to handle. We take the stress and strain away from them that complaints present! check out our website www.harbourlinkassist.co.uk - blue features as our corporate colors. The business is 26 years old so well established in the industry. The reverse of the flyer will be printed with endorsements from current company clients. I would like something light hearted projecting the relief of pressure we can provide whilst also suggesting complaints and complainants will be in professional safe capable hands

Industry/Entity Type

Travel

```html
<!DOCTYPE html>
<html lang="en">
<head>
<meta charset="utf-8">
<title>Harbourlink Assist – Customer Complaints Flyer</title>
<link rel="stylesheet" href="https://fonts.googleapis.com/css2?family=Libre+Baskerville:wght@400;700&family=Open+Sans:wght@400;600;800&family=Barlow:wght@400&display=swap">
<style>
  :root {
    --brand-blue: #1273c6;
    --brand-blue-deep: #0d5fa8;
    --ink: #111111;
    --muted: #9a9a9a;
    --paper: #ffffff;
    --stage: #eceef1;
  }
  * { box-sizing: border-box; margin: 0; padding: 0; }
  html, body { width: 848px; height: 1200px; overflow: hidden; background: var(--stage); }
  body { position: relative; font-family: "Open Sans", sans-serif; }

  .flyer {
    position: absolute; top: 160px; width: 390px; height: 880px;
    background: var(--paper); overflow: hidden;
    box-shadow: 0 2px 10px rgba(0,0,0,0.12);
  }
  .flyer--front { left: 22px; }
  .flyer--back { left: 436px; }

  /* Front */
  .headline { text-align: center; padding-top: 26px; font-family: "Libre Baskerville", serif; font-weight: 700; line-height: 1.02; }
  .headline__blue { color: var(--brand-blue); font-size: 40px; letter-spacing: 0.5px; }
  .headline__dark { color: var(--ink); font-size: 37px; }
  .tagline { text-align: center; margin-top: 18px; font-family: "Libre Baskerville", serif; font-size: 12px; color: var(--ink); letter-spacing: 0.3px; }
  .tagline span { color: var(--brand-blue); font-size: 15px; }
  .hero-photo {
    position: absolute; top: 168px; left: 0; width: 100%; height: 352px;
    background: linear-gradient(180deg, #f4f4f4 0%, #dcdcdc 55%, #b88a5a 78%, #c9996a 100%);
  }
  .brand-band {
    position: absolute; top: 520px; left: 0; width: 100%; height: 128px;
    background: var(--brand-blue); color: var(--paper); text-align: center; padding-top: 34px;
  }
  .brand-band__name { font-family: "Open Sans", sans-serif; font-weight: 400; font-size: 34px; letter-spacing: 0.5px; }
  .brand-band__sub { font-size: 12px; margin-top: 2px; letter-spacing: 0.4px; }
  .contact { position: absolute; top: 680px; left: 30px; font-family: "Barlow", sans-serif; font-size: 17px; line-height: 29px; color: var(--brand-blue); }
  .contact b { display: inline-block; width: 20px; font-weight: 400; color: var(--muted); }

  /* Back */
  .rep-title { margin: 22px 0 0 24px; font-family: "Open Sans", sans-serif; font-weight: 800; font-size: 21px; letter-spacing: -0.3px; color: var(--brand-blue); }
  .rep-title span { color: var(--muted); }
  .testimonial {
    margin: 12px 16px 0; background: var(--brand-blue); color: var(--paper);
    border-radius: 16px; padding: 12px 20px 14px; font-size: 11.5px; line-height: 1.35; text-align: center;
  }
  .testimonial__quote { font-weight: 600; }
  .testimonial__source { text-align: left; margin-top: 8px; padding-top: 6px; border-top: 3px solid var(--paper); font-size: 11.5px; }
  .rating { position: absolute; top: 632px; left: 0; width: 100%; height: 140px; }
  .rating__list { position: absolute; left: 54px; top: 22px; font-size: 19px; line-height: 26px; color: var(--ink); text-align: right; width: 140px; }
  .rating__list li { list-style: none; }
  .rating__box { display: inline-block; width: 15px; height: 15px; border: 1.6px solid var(--ink); margin-left: 12px; vertical-align: -1px; }
  .rating__art { position: absolute; right: 0; top: 0; width: 170px; height: 140px; background: linear-gradient(135deg, #f6f6f6 0%, #d9d9d9 45%, #33363c 100%); }
  .back-footer { position: absolute; top: 790px; left: 22px; right: 16px; height: 80px; display: flex; }
  .back-footer__brand { width: 130px; color: var(--brand-blue); font-size: 21px; line-height: 1.05; padding-top: 4px; }
  .back-footer__brand small { display: block; font-size: 8px; margin-top: 4px; }
  .back-footer__rule { width: 2px; background: var(--brand-blue); margin-right: 14px; }
  .back-footer .contact { position: static; font-size: 13.5px; line-height: 19px; padding-top: 4px; }
  .back-footer .contact b { width: 16px; }
</style>
</head>
<body>

<section class="flyer flyer--front">
  <h1 class="headline">
    <div class="headline__blue">CUSTOMER</div>
    <div class="headline__dark">COMPLAINTS?</div>
  </h1>
  <p class="tagline">WE WILL TAKE AWAY <span>THE STRESS</span></p>
  <div class="hero-photo" role="img" aria-label="Photo of a stressed businessman at his desk pulling a telephone receiver away on its cord"></div>
  <div class="brand-band">
    <div class="brand-band__name">Harbourlink Assist</div>
    <div class="brand-band__sub">Customer Service &amp; Training Specialists</div>
  </div>
  <div class="contact">
    <div><b>t</b>020 7946 0183</div>
    <div><b>f</b>020 7946 0184</div>
    <div><b>e</b>help@harbourlinkassist.co.uk</div>
    <div><b>w</b>www.harbourlinkassist.co.uk</div>
  </div>
</section>

<section class="flyer flyer--back">
  <h2 class="rep-title">OUR HARD EARNED <span>REPUTATION</span></h2>

  <article class="testimonial">
    <p class="testimonial__quote">“Our members have made use of and appreciated the knowledge and experience of the team at Harbourlink Assist over many years. The training courses provided by Sofia for ABTO always receive very good reviews.”</p>
    <p class="testimonial__source">Maria Holloway<br>Partnership and Events Manager<br>Alliance of Boutique Tour Operators</p>
  </article>

  <article class="testimonial">
    <p class="testimonial__quote">‘It is great to have the support of Marion and her colleagues when the going gets rough. Happily we do not have to call upon them often but we have received excellent service from them over the years when we have needed help. We are happy to endorse Harbourlink Assist.’</p>
    <p class="testimonial__source">Clara Benning<br>Northern Steppe Journeys</p>
  </article>

  <article class="testimonial">
    <p class="testimonial__quote">‘We have found the experience and knowledge of the team at Harbourlink Assist invaluable with the more complex claims that arise from time to time’.</p>
    <p class="testimonial__source">Daniel Ashford<br>Head of Customer Support<br>WayPoint Travel</p>
  </article>

  <div class="rating">
    <ul class="rating__list">
      <li>EXCELLENT<span class="rating__box"></span></li>
      <li>GOOD<span class="rating__box"></span></li>
      <li>AVERAGE<span class="rating__box"></span></li>
      <li>POOR<span class="rating__box"></span></li>
    </ul>
    <div class="rating__art" role="img" aria-label="Photo of a hand with a red marker ticking a hand-lettered 'Awesome!!' option above the rating list"></div>
  </div>

  <footer class="back-footer">
    <div class="back-footer__brand">Harbourlink<br>Assist<small>Customer Service &amp; Training Specialists</small></div>
    <div class="back-footer__rule"></div>
    <div class="contact">
      <div><b>t</b>020 7946 0183</div>
      <div><b>f</b>020 7946 0184</div>
      <div><b>e</b>help@harbourlinkassist.co.uk</div>
      <div><b>w</b>harbourlinkassist.co.uk</div>
    </div>
  </footer>
</section>

</body>
</html>
```